Bex2Court Sign

Sign will be used to advertise my personal injury law firm. Sign will be 4' x 8'. With that in mind, I want it to pop, but not too busy. I have two logos I use, so feel free to incorporate either of those. I have attached a couple photos of me to choose from, the two logos (use one if it fits), and I want the sign to say something to the effect of "Car Accident?" Call me. Ask for Bex. 866-BEX2CRT." I have also attached a sign design that I had made on another project. Feel free to use for inspiration.
Updates

I appreciate all the designs, but pretty much every one looks the same. I was hoping for some variety. It looks like most of the designers are using the same template. I know the sign is small, so it doesn't allow for much. But I have updated my "brief" and included some examples of signs that stood out to me. Hope this helps.

Requirements
Must have
• Car Accident?
Call me. Ask for Bex.
866-BEX2CRT
Veteran Owned
Photo of me
Nice to have
• My Bex2Court logo

```html
<!DOCTYPE html>
<html lang="en">
<head>
<meta charset="utf-8">
<title>Bex2Court Sign</title>
<link rel="stylesheet" href="https://fonts.googleapis.com/css2?family=Roboto+Slab:wght@400;600;700;800&family=Open+Sans:wght@600;700&display=swap">
<style>
  :root {
    --forest: #2b5a1e;
    --teal: #0c5266;
    --teal-deep: #11605a;
    --white: #ffffff;
    --mist: #ececec;
    --stage: #0b0b0b;
    --photo-light: #d4d4d4;
    --photo-dark: #3a3a3a;
  }
  * { margin: 0; padding: 0; box-sizing: border-box; }
  html, body {
    width: 1018px; height: 1200px; overflow: hidden;
    background: var(--stage);
  }
  .sign {
    position: absolute;
    left: 29px; top: 360px;
    width: 1546px; height: 773px;
    transform: scale(0.621);
    transform-origin: top left;
    background: var(--white);
    overflow: hidden;
    font-family: "Roboto Slab", Georgia, serif;
  }
  .sign > * { white-space: nowrap; }
  .backdrop {
    position: absolute; left: 560px; top: 0; width: 986px; height: 773px;
    background: linear-gradient(100deg, rgba(255,255,255,1) 0%, var(--mist) 45%, #dcdcdc 75%, #f2f2f2 100%);
  }
  .phone-band {
    position: absolute; left: 0; top: 635px; width: 1546px; height: 138px;
    background: var(--teal);
  }
  .portrait {
    position: absolute; left: 880px; top: 60px; width: 590px; height: 713px;
    background: radial-gradient(ellipse at 50% 28%, var(--photo-light) 0%, #8a8a8a 45%, var(--photo-dark) 100%);
    border-radius: 200px 200px 0 0;
  }
  .brand {
    position: absolute; left: 85px; top: 70px;
    color: var(--forest);
    font-weight: 400; font-size: 100px; line-height: 1;
  }
  .brand-tagline {
    position: absolute; left: 310px; top: 190px;
    font-family: "Open Sans", Arial, sans-serif;
    font-weight: 600; font-size: 18px; letter-spacing: 4px;
    color: var(--teal);
  }
  .brand-tagline strong { font-weight: 700; }
  .headline-car {
    position: absolute; left: 60px; top: 210px;
    color: var(--forest);
    font-weight: 700; font-size: 370px; line-height: 1;
    letter-spacing: -8px;
  }
  .headline-strip {
    position: absolute; left: 190px; top: 368px; width: 690px; height: 58px;
    background: var(--white);
  }
  .headline-accident {
    position: absolute; left: 200px; top: 374px;
    color: var(--teal);
    font-weight: 800; font-size: 50px; line-height: 1;
    letter-spacing: 26px;
  }
  .call-line {
    position: absolute; left: 85px; top: 540px;
    color: var(--teal);
    font-weight: 600; font-size: 72px; line-height: 1;
  }
  .phone {
    position: absolute; left: 80px; top: 658px;
    color: var(--white);
    font-weight: 800; font-size: 92px; line-height: 1;
    letter-spacing: -2px;
  }
  .veteran-badge {
    position: absolute; left: 1262px; top: -70px; width: 290px; height: 288px;
    border-radius: 50%;
    background: linear-gradient(135deg, var(--forest), var(--teal-deep));
  }
  .veteran-text {
    position: absolute; left: 1300px; top: 28px; width: 230px;
    color: var(--white); text-align: center;
    font-weight: 600; font-size: 48px; line-height: 66px;
  }
</style>
</head>
<body>
  <main class="sign">
    <div class="backdrop"></div>
    <div class="phone-band"></div>
    <div class="portrait" role="img" aria-label="Black and white portrait of the attorney in a suit jacket and white shirt"></div>

    <div class="brand">Bex2Court</div>
    <div class="brand-tagline">GO WITH THE <strong>BEX</strong></div>

    <div class="headline-car">CAR</div>
    <div class="headline-strip"></div>
    <div class="headline-accident">ACCIDENT?</div>

    <div class="call-line">Call me. Ask for Bex.</div>
    <div class="phone">866-BEX2CRT</div>

    <div class="veteran-badge"></div>
    <div class="veteran-text">Veteran<br>Owned</div>
  </main>
</body>
</html>
```